New Flyer Design Project

Needing brochure explaining the benefits of a home sleep study compared to a clinical hospital sleep study. We had our company logo designed by Lumen Forge, we love it. We would like for it to be a bi-fold. See attachments for examples of information we would like to include.

```html
<!DOCTYPE html>
<html lang="en">
<head>
<meta charset="utf-8">
<title>Prairie Rest CPAP – Home Sleep Study Bi-fold</title>
<link href="https://fonts.googleapis.com/css2?family=Bebas+Neue&family=Montserrat:wght@500;600;700;800&display=swap" rel="stylesheet">
<style>
:root{
  --navy:#123f8c;
  --navy-dark:#0e3272;
  --green:#5aae32;
  --blue:#1565c8;
  --ink:#1b2f5c;
  --paper:#ffffff;
  --backdrop:#e4e6ea;
  --grey-icon:#8a8d93;
  --photo-light:#e9ecf1;
  --photo-mid:#cfd5de;
}
*{box-sizing:border-box;margin:0;padding:0}
html,body{width:1200px;height:3069px;overflow:hidden}
body{background:var(--backdrop);font-family:'Montserrat',sans-serif;color:var(--ink);position:relative}
.spread{position:absolute;left:50px;width:1100px;height:784px;background:var(--paper);box-shadow:0 6px 18px rgba(0,0,0,.18);overflow:hidden}
.spread--outer{top:680px}
.spread--inner{top:1604px}
.abs{position:absolute}

/* ---------- outer spread: back panel ---------- */
.back-panel{left:0;top:0;width:550px;height:784px}
.back-panel__band{left:0;top:475px;width:550px;height:309px;background:var(--navy)}
.brand{display:flex;align-items:center;gap:12px}
.brand__dot{width:34px;height:34px;border-radius:50%;background:var(--green);flex:none}
.brand__name{font-weight:800;font-size:34px;line-height:1.05;color:var(--navy);white-space:nowrap}
.brand--light .brand__name{color:#fff}
.back-panel .brand{left:60px;top:52px}
.back-panel__rule{left:60px;top:150px;width:430px;height:3px;background:var(--green)}
.headline{left:52px;top:180px;font-weight:800;font-size:29px;line-height:1.1;color:var(--navy);text-transform:uppercase;white-space:nowrap}
.body-copy{left:52px;width:450px;font-size:12.5px;line-height:1.4;font-weight:600;color:var(--navy)}
.body-copy--a{top:262px}
.body-copy--b{top:320px}
.checklist-title{left:46px;top:400px;font-weight:800;font-size:22px;line-height:1.1;color:var(--navy);white-space:nowrap}
.checklist-title span{color:var(--green);display:block}
.checklist{left:46px;top:462px;width:466px;height:104px;background:#fff;border:2px dashed var(--green);border-radius:10px;padding:10px 10px;display:grid;grid-template-columns:240px 1fr;column-gap:10px;row-gap:4px;font-size:12.5px;font-weight:600;color:var(--navy)}
.checklist li{list-style:none;display:flex;gap:6px;line-height:1.25}
.checklist li::before{content:"";width:10px;height:10px;border:1px solid var(--navy);flex:none;margin-top:3px}
.checklist-note{left:46px;top:588px;width:290px;font-size:12px;font-weight:700;color:#fff;line-height:1.3}
.cta{left:340px;top:583px;width:170px;height:32px;border-radius:6px;background:var(--green);color:#fff;font-size:11.5px;font-weight:700;display:flex;align-items:center;justify-content:center}
.contact{left:40px;top:688px;list-style:none;color:#fff;font-size:14px;font-weight:600}
.contact li{display:flex;align-items:center;gap:12px;height:25px}
.contact svg{width:14px;height:14px;flex:none}

/* ---------- outer spread: cover panel ---------- */
.cover-panel{left:550px;top:0;width:550px;height:784px;background:linear-gradient(180deg,#f3f4f6,#e8eaee)}
.cover-title{left:40px;top:30px;font-weight:800;font-size:45px;line-height:1.05;color:var(--navy);white-space:nowrap}
.cover-title span{color:var(--green);display:block}
.cover-tagline{left:40px;top:142px;font-size:20px;font-weight:600;color:var(--navy)}
.cover-photo{left:0;top:180px;width:550px;height:380px;background:linear-gradient(135deg,var(--photo-light),var(--photo-mid) 60%,#dfe3ea)}
.cover-curve{left:0;top:400px;width:550px;height:384px}
.cover-panel .brand{left:70px;top:600px}
.cover-panel .brand__name{font-size:32px}
.delivery{left:70px;top:710px;width:430px;height:60px;border-radius:8px;background:var(--navy-dark);display:flex;align-items:center;gap:16px;padding:0 18px;color:#fff;font-size:15.5px;font-weight:600;line-height:1.2}
.delivery svg{width:44px;height:30px;flex:none}

/* ---------- inner spread ---------- */
.inner-header{left:0;top:0;width:1100px;height:178px;background:var(--navy)}
.compare-title{top:16px;font-family:'Bebas Neue',sans-serif;font-weight:400;font-size:56px;color:#fff;letter-spacing:.5px;line-height:1.1;white-space:nowrap}
.compare-title--home{left:100px}
.compare-title--clinic{left:618px}
.vs-badge{left:512px;top:18px;width:66px;height:66px;border-radius:50%;background:var(--green);color:#fff;font-family:'Bebas Neue',sans-serif;font-size:38px;line-height:1;padding-top:4px;display:flex;align-items:center;justify-content:center}
.compare-sub{left:0;top:94px;width:1100px;text-align:center;font-weight:700;font-size:30px;color:var(--green);white-space:nowrap}
.tab{top:140px;width:490px;height:48px;border-radius:24px 24px 0 0;color:#fff;font-weight:700;font-size:24px;display:flex;align-items:center;justify-content:center}
.tab--home{left:35px;background:var(--green)}
.tab--clinic{left:570px;background:var(--blue)}
.tab-base{left:0;top:186px;width:1100px;height:4px;background:var(--navy)}
.compare-col{top:200px;width:490px}
.compare-col--home{left:35px}
.compare-col--clinic{left:570px}
.feature{position:relative;height:80px;border-bottom:1px solid #d4d8e0;display:flex;align-items:center;gap:14px;padding-left:4px}
.feature:last-child{border-bottom:none}
.feature__icon{width:46px;height:46px;border-radius:50%;background:var(--navy);border:3px solid #c9d3e6;display:flex;align-items:center;justify-content:center;flex:none}
.feature__icon svg{width:24px;height:24px}
.feature__name{font-size:20px;font-weight:700;color:var(--green);line-height:1.1}
.feature__desc{font-size:12px;font-weight:600;color:var(--navy);line-height:1.2;width:240px}
.feature__art{position:absolute;right:20px;top:12px}
.art-photo{width:90px;height:56px;background:linear-gradient(135deg,#cfd3d8,#9aa0a8)}
.art-photo--box{width:70px;height:56px;background:linear-gradient(135deg,#d9b07a,#b9894f)}
.art-photo--lab{width:120px;height:60px;right:0;top:8px;background:linear-gradient(135deg,#6f7d92,#3c4658)}
.product-title{left:35px;top:585px;font-weight:800;font-size:21px;color:var(--green);white-space:nowrap}
.product-sub{left:35px;top:617px;font-size:11.5px;font-weight:600;color:var(--navy)}
.ticks{left:35px;top:645px;list-style:none;font-size:15px;font-weight:700;color:var(--navy)}
.ticks li{display:flex;align-items:center;gap:12px;height:26px}
.ticks svg{width:15px;height:15px}
.inner-photo{left:550px;top:548px;width:550px;height:214px;background:linear-gradient(120deg,var(--photo-light),var(--photo-mid) 55%,#e3d6cc)}
.inner-base{left:0;top:762px;width:1100px;height:22px;background:var(--green)}
</style>
</head>
<body>

<section class="spread spread--outer">
  <div class="abs back-panel">
    <div class="abs back-panel__band"></div>
    <div class="abs brand">
      <span class="brand__dot"></span>
      <span class="brand__name">Prairie Rest CPAP<br>&amp; Sleep Care</span>
    </div>
    <div class="abs back-panel__rule"></div>
    <h2 class="abs headline">80% of sleep apnea<br>cases go undiagnosed.</h2>
    <p class="abs body-copy body-copy--a">Your wake up exhausted. You fall asleep at your desk. Your partner says you stop breathing at night. You know something's wrong.</p>
    <p class="abs body-copy body-copy--b">Most people wait years before getting tested because sleep labs are expensive, inconvenient, and scheduled months out. Meanwhile you're crashing your car, destroying your health, and feeling like garbage every single day.</p>
    <h3 class="abs checklist-title">SELF ASSESSMENT CHECKLIST<span>DO YOU</span></h3>
    <ul class="abs checklist">
      <li>Snore loudly</li>
      <li>Wake up with headaches?</li>
      <li>Wake up gasping or choking?</li>
      <li>Feel tired no matter how much you sleep?</li>
      <li>Fall asleep during the day even when you slept 8 hours?</li>
    </ul>
    <p class="abs checklist-note">If you checked 2 boxes, you probably have sleep apnea. Stop guessing. Get tested.</p>
    <div class="abs cta">Take the sleep quiz now</div>
    <ul class="abs contact">
      <li><svg viewBox="0 0 16 16"><path d="M3 1l3 3-2 2c1 2 3 4 5 5l2-2 3 3-2 3C7 15 1 9 1 3z" fill="none" stroke="#fff" stroke-width="1.4"/></svg>(555) 014-2290</li>
      <li><svg viewBox="0 0 16 16"><circle cx="8" cy="8" r="6.5" fill="none" stroke="#fff" stroke-width="1.3"/><path d="M1.5 8h13M8 1.5c-3 3.5-3 9.5 0 13M8 1.5c3 3.5 3 9.5 0 13" fill="none" stroke="#fff" stroke-width="1.1"/></svg>prairierestsleep.example</li>
      <li><svg viewBox="0 0 16 16"><path d="M8 15s5-5 5-9A5 5 0 0 0 3 6c0 4 5 9 5 9z" fill="none" stroke="#fff" stroke-width="1.3"/><circle cx="8" cy="6" r="1.8" fill="#fff"/></svg>Local care. Better sleep. Healthier lives.</li>
    </ul>
  </div>

  <div class="abs cover-panel">
    <h1 class="abs cover-title">BETTER SLEEP<span>STARTS AT HOME</span></h1>
    <p class="abs cover-tagline">Simple. Comfortable. Effective.</p>
    <div class="abs cover-photo" role="img" aria-label="Photo of a woman sleeping peacefully on white pillows and bedding"></div>
    <svg class="abs cover-curve" viewBox="0 0 550 384" preserveAspectRatio="none">
      <path d="M0 150 C180 140 400 110 550 0 L550 384 L0 384Z" fill="var(--green)"/>
      <path d="M0 165 C180 155 400 125 550 16 L550 384 L0 384Z" fill="var(--navy)"/>
    </svg>
    <div class="abs brand brand--light">
      <span class="brand__dot"></span>
      <span class="brand__name">Prairie Rest CPAP<br>&amp; Sleep Care</span>
    </div>
    <div class="abs delivery">
      <svg viewBox="0 0 44 30"><path d="M2 5h24v17H2zM26 11h9l6 6v5H26z" fill="none" stroke="var(--green)" stroke-width="2"/><circle cx="10" cy="24" r="3.5" fill="var(--navy-dark)" stroke="var(--green)" stroke-width="2"/><circle cx="34" cy="24" r="3.5" fill="var(--navy-dark)" stroke="var(--green)" stroke-width="2"/></svg>
      <span>We deliver. You sleep.<br>We help you feel like yourself again.</span>
    </div>
  </div>
</section>

<section class="spread spread--inner">
  <div class="abs inner-header"></div>
  <h2 class="abs compare-title compare-title--home">HOME SLEEP STUDY</h2>
  <div class="abs vs-badge">VS</div>
  <h2 class="abs compare-title compare-title--clinic">CLINICAL SLEEP STUDY</h2>
  <p class="abs compare-sub">The Smarter Way to Get Answers</p>
  <div class="abs tab tab--home">Home Sleep Study</div>
  <div class="abs tab tab--clinic">Clinical Sleep Study</div>

  <div class="abs compare-col compare-col--home">
    <div class="feature">
      <span class="feature__icon"><svg viewBox="0 0 24 24"><circle cx="12" cy="12" r="8" fill="none" stroke="#fff" stroke-width="2"/><path d="M8 12l3 3 5-6" fill="none" stroke="#fff" stroke-width="2"/></svg></span>
      <div><div class="feature__name">Comfortable</div><div class="feature__desc">A minimal device with<br>2 wire and 3 sensors</div></div>
      <div class="feature__art art-photo" role="img" aria-label="Photo of the compact home sleep test device"></div>
    </div>
    <div class="feature">
      <span class="feature__icon"><svg viewBox="0 0 24 24"><path d="M4 12l8-7 8 7v8H4z" fill="none" stroke="#fff" stroke-width="2"/></svg></span>
      <div><div class="feature__name">Convenient</div><div class="feature__desc">Delivered to you door-sleep<br>in your own bed at home</div></div>
      <div class="feature__art art-photo art-photo--box" role="img" aria-label="Photo of a cardboard shipping box"></div>
    </div>
    <div class="feature">
      <span class="feature__icon"><svg viewBox="0 0 24 24"><rect x="4" y="6" width="16" height="14" rx="2" fill="none" stroke="#fff" stroke-width="2"/><path d="M4 10h16M8 3v5M16 3v5" stroke="#fff" stroke-width="2"/></svg></span>
      <div><div class="feature__name">Accessible</div><div class="feature__desc">Scheduling and device delivery<br>in 2-4 business deys</div></div>
      <svg class="feature__art" width="52" height="52" viewBox="0 0 52 52"><rect x="3" y="8" width="46" height="40" rx="5" fill="var(--green)"/><rect x="13" y="2" width="5" height="12" rx="2" fill="var(--green)"/><rect x="34" y="2" width="5" height="12" rx="2" fill="var(--green)"/><g fill="#fff"><rect x="10" y="20" width="8" height="7"/><rect x="22" y="20" width="8" height="7"/><rect x="34" y="20" width="8" height="7"/><rect x="10" y="32" width="8" height="7"/><rect x="22" y="32" width="8" height="7"/><rect x="34" y="32" width="8" height="7"/></g></svg>
    </div>
    <div class="feature">
      <span class="feature__icon"><svg viewBox="0 0 24 24"><circle cx="12" cy="12" r="8" fill="none" stroke="#fff" stroke-width="2"/><text x="12" y="16" font-size="11" font-family="Montserrat,sans-serif" font-weight="700" fill="#fff" text-anchor="middle">$</text></svg></span>
      <div><div class="feature__name">Affordable</div><div class="feature__desc">Pay a one-time flat fee<br>os $ 189</div></div>
      <svg class="feature__art" width="52" height="56" viewBox="0 0 52 56"><g transform="rotate(-35 26 28)"><path d="M16 12h20v36H16z" fill="var(--green)"/><circle cx="26" cy="17" r="3" fill="#fff"/><text x="26" y="38" font-size="10" font-family="Montserrat,sans-serif" font-weight="700" fill="#fff" text-anchor="middle">$189</text></g></svg>
    </div>
  </div>

  <div class="abs compare-col compare-col--clinic">
    <div class="feature">
      <span class="feature__icon"><svg viewBox="0 0 24 24"><circle cx="12" cy="8" r="4" fill="none" stroke="#fff" stroke-width="2"/><path d="M5 21c0-5 3-7 7-7s7 2 7 7" fill="none" stroke="#fff" stroke-width="2"/></svg></span>
      <div><div class="feature__name">Invasive</div><div class="feature__desc">20-30 wires attached all<br>over your body</div></div>
      <div class="feature__art art-photo art-photo--lab" role="img" aria-label="Photo of a patient wired up for a lab sleep study"></div>
    </div>
    <div class="feature">
      <span class="feature__icon"><svg viewBox="0 0 24 24"><circle cx="12" cy="12" r="7" fill="none" stroke="#fff" stroke-width="2" stroke-dasharray="4 2"/><circle cx="12" cy="12" r="2.5" fill="#fff"/></svg></span>
      <div><div class="feature__name">Disruptive</div><div class="feature__desc">Must sleep in a lab overnight<br>and requires travel</div></div>
      <svg class="feature__art" width="50" height="56" viewBox="0 0 50 56"><rect x="6" y="14" width="38" height="40" fill="var(--grey-icon)"/><rect x="16" y="2" width="18" height="14" fill="var(--grey-icon)"/><path d="M25 5v8M21 9h8" stroke="#fff" stroke-width="2.5"/><g fill="#fff"><rect x="11" y="20" width="6" height="6"/><rect x="22" y="20" width="6" height="6"/><rect x="33" y="20" width="6" height="6"/><rect x="11" y="31" width="6" height="6"/><rect x="33" y="31" width="6" height="6"/><rect x="21" y="40" width="8" height="14"/></g></svg>
    </div>
    <div class="feature">
      <span class="feature__icon"><svg viewBox="0 0 24 24"><rect x="4" y="6" width="16" height="14" rx="2" fill="none" stroke="#fff" stroke-width="2"/><path d="M4 10h16" stroke="#fff" stroke-width="2"/></svg></span>
      <div><div class="feature__name">Hard to schedule</div><div class="feature__desc">Scheduling can take anywhere from 3<br>weeks to 6 months</div></div>
      <svg class="feature__art" width="50" height="50" viewBox="0 0 50 50"><circle cx="25" cy="25" r="20" fill="none" stroke="var(--grey-icon)" stroke-width="5"/><path d="M25 13v13h9" fill="none" stroke="var(--grey-icon)" stroke-width="4"/></svg>
    </div>
    <div class="feature">
      <span class="feature__icon"><svg viewBox="0 0 24 24"><rect x="5" y="5" width="14" height="14" rx="2" fill="none" stroke="#fff" stroke-width="2"/><text x="12" y="16" font-size="10" font-family="Montserrat,sans-serif" font-weight="700" fill="#fff" text-anchor="middle">$</text></svg></span>
      <div><div class="feature__name">Expensive</div><div class="feature__desc">Fees can range from $500-$10,000</div></div>
      <svg class="feature__art" width="46" height="56" viewBox="0 0 46 56"><path d="M16 4h14l-4 10c10 4 17 14 17 26 0 10-8 14-20 14S3 50 3 40C3 28 10 18 20 14z" fill="var(--grey-icon)"/><text x="23" y="45" font-size="20" font-family="Montserrat,sans-serif" font-weight="700" fill="#fff" text-anchor="middle">$</text></svg>
    </div>
  </div>

  <h3 class="abs product-title">RESTCHECK ONE HOME SLEEP TEST</h3>
  <p class="abs product-sub">No appointments. No insurance chaos. just better sleep,made easy</p>
  <ul class="abs ticks">
    <li><svg viewBox="0 0 16 16"><circle cx="8" cy="8" r="8" fill="var(--green)"/><path d="M4.5 8.2l2.3 2.3 4.5-4.8" fill="none" stroke="#fff" stroke-width="1.8"/></svg>FDA Cleared Device, DOT Approved.</li>
    <li><svg viewBox="0 0 16 16"><circle cx="8" cy="8" r="8" fill="var(--green)"/><path d="M4.5 8.2l2.3 2.3 4.5-4.8" fill="none" stroke="#fff" stroke-width="1.8"/></svg>Results in less than 72 Hours</li>
    <li><svg viewBox="0 0 16 16"><circle cx="8" cy="8" r="8" fill="var(--green)"/><path d="M4.5 8.2l2.3 2.3 4.5-4.8" fill="none" stroke="#fff" stroke-width="1.8"/></svg>98 Percent Lab Accuracy.</li>
  </ul>
  <div class="abs inner-photo" role="img" aria-label="Photo of a woman asleep on a white pillow under a light blanket"></div>
  <div class="abs inner-base"></div>
</section>

</body>
</html>
```